The Harvest Compass

Cutting Through the Noise to What Actually Works.

Nutrition book

Target Market(s)

People looking to be or get healthy and eat right.

```html
<!DOCTYPE html>
<html lang="en">
<head>
<meta charset="UTF-8">
<title>The Harvest Compass</title>
<link href="https://fonts.googleapis.com/css2?family=Archivo:wght@800&family=Bebas+Neue&family=Barlow:wght@300;700&display=swap" rel="stylesheet">
<style>
  :root {
    --backdrop: #242424;
    --cover-light: #5c1c25;
    --cover-dark: #360c12;
    --cream: #efe6d6;
    --photo-light: #6a2a30;
    --photo-dark: #4a1419;
  }
  * { margin: 0; padding: 0; box-sizing: border-box; }
  html, body {
    width: 1200px; height: 1200px; overflow: hidden;
    background: var(--backdrop);
  }
  .cover {
    position: absolute; left: 180px; top: 50px;
    width: 840px; height: 1100px;
    overflow: hidden;
    background: radial-gradient(ellipse at 30% 35%, var(--cover-light), var(--cover-dark) 85%);
    color: var(--cream);
  }
  .title {
    position: absolute; left: 96px; top: 104px;
    font-family: "Archivo", sans-serif; font-weight: 800;
    line-height: 0.98; text-transform: uppercase;
  }
  .title-article { display: block; font-size: 34px; letter-spacing: 2px; margin-bottom: 6px; }
  .title-main { display: block; font-size: 74px; letter-spacing: 1px; }
  .cover-photo {
    position: absolute; left: 190px; top: 360px;
    width: 560px; height: 380px;
    border-radius: 12px;
    background: radial-gradient(ellipse at 45% 50%, var(--photo-light), var(--photo-dark) 90%);
  }
  .hierarchy-list {
    position: absolute; left: 96px; top: 780px;
    list-style: none;
    font-family: "Bebas Neue", sans-serif;
    font-size: 40px; letter-spacing: 2px; line-height: 46px;
  }
  .hierarchy-list li:nth-child(2) { padding-left: 20px; }
  .hierarchy-list li:nth-child(3) { padding-left: 40px; }
  .hierarchy-list li:nth-child(4) { padding-left: 60px; }
  .hierarchy-list li:nth-child(5) { padding-left: 80px; }
  .hierarchy-list li:nth-child(6) { padding-left: 100px; }
  .tagline {
    position: absolute; right: 80px; top: 940px;
    font-family: "Barlow", sans-serif; font-size: 24px; line-height: 1.3;
  }
  .tagline-lead { display: block; font-weight: 300; }
  .tagline-close { display: block; font-weight: 700; }
</style>
</head>
<body>
  <main class="cover">
    <h1 class="title">
      <span class="title-article">The</span>
      <span class="title-main">Harvest</span>
      <span class="title-main">Compass</span>
    </h1>
    <div class="cover-photo" role="img" aria-label="Photo of a steel pan holding roasted sweet potato cubes, sliced grilled chicken and green beans, beside a row of nested measuring spoons"></div>
    <ul class="hierarchy-list">
      <li>Calories</li>
      <li>Protein</li>
      <li>Food Quality</li>
      <li>Meal Timing</li>
      <li>Supplements</li>
      <li>Noise</li>
    </ul>
    <p class="tagline">
      <span class="tagline-lead">Cutting Through the Noise</span>
      <span class="tagline-close">to What Actually Works.</span>
    </p>
  </main>
</body>
</html>
```